BLQ Business Card

We need a business card that reflect our business, we have put anther business card as an example of what we like but please feel free to do your own thing.

Here are the items to be placed on card

Wade Pelham
Amber Harbor Supply
Mobile: 917-555-4820
Office: 516-555-7164
Fax: 866-555-3291
Email: info@amberharborsupply-example.com
Website: amberharborsupply-example.com

I have added raw files to upload

Wade Pelham
Amber Harbor Supply
Mobile: 917-555-4820
Office: 516-555-7164
Fax: 866-555-3291 

Target Market(s)

Natural product manufactures, and retailers and distributors

Industry/Entity Type

Business

Requirements
Must have
• 1. Logo
2. The colors of the company

```html
<!DOCTYPE html>
<html lang="en">
<head>
<meta charset="utf-8">
<title>BLQ Business Card</title>
<link rel="stylesheet" href="https://fonts.googleapis.com/css2?family=Arimo:wght@400;700&display=swap">
<style>
  :root {
    --green: #6cb30f;
    --black: #0c0c0c;
    --white: #ffffff;
    --backdrop: #d4d4d4;
    --ink: #111111;
  }
  * { box-sizing: border-box; margin: 0; padding: 0; }
  html, body { width: 1200px; height: 985px; overflow: hidden; }
  body {
    background: var(--backdrop);
    font-family: "Arimo", Arial, sans-serif;
    position: relative;
  }
  .card {
    position: absolute;
    left: 250px;
    width: 700px;
    height: 400px;
    background: var(--white);
    overflow: hidden;
    box-shadow: 0 6px 18px rgba(0,0,0,0.18);
  }
  .card--back { top: 60px; }
  .card--front { top: 525px; }

  .top-rule {
    position: absolute; top: 0; left: 0; right: 0;
    height: 14px; background: var(--black);
  }

  /* back side */
  .back-mark {
    position: absolute; left: 0; right: 0; top: 140px;
    display: flex; justify-content: center; align-items: center; gap: 14px;
  }
  .back-mark__square { width: 34px; height: 34px; background: var(--green); }
  .back-mark__name {
    font-weight: 700; font-size: 64px; color: var(--black); letter-spacing: 2px;
  }
  .back-url {
    position: absolute; left: 0; right: 0; top: 250px;
    text-align: center; font-weight: 700; font-size: 20px; color: var(--ink);
  }
  .back-url .accent { color: var(--green); }
  .bottom-rule {
    position: absolute; bottom: 0; left: 0; right: 0; height: 14px;
    display: flex;
  }
  .bottom-rule span:nth-child(1) { flex: 3; background: var(--green); }
  .bottom-rule span:nth-child(2) { flex: 3; background: var(--black); }
  .bottom-rule span:nth-child(3) { flex: 4; background: var(--green); }

  /* front side */
  .front-brand {
    position: absolute; right: 40px; top: 60px;
    display: flex; align-items: center; gap: 12px;
  }
  .front-brand__square { width: 26px; height: 26px; background: var(--green); }
  .front-brand__name { font-weight: 700; font-size: 40px; color: var(--green); }

  .name-band {
    position: absolute; left: 0; right: 0; top: 170px; height: 46px;
    background: var(--black); color: var(--white);
    display: flex; align-items: center; padding: 0 40px;
  }
  .name-band__person { font-weight: 700; font-size: 22px; letter-spacing: 1px; text-transform: uppercase; }
  .name-band__company { margin-left: auto; font-size: 20px; }

  .email-row {
    position: absolute; left: 0; right: 0; top: 216px; height: 62px;
    display: flex; align-items: center; padding: 0 40px;
    font-size: 20px; color: var(--ink);
  }
  .label { font-weight: 700; }

  .contact-row {
    position: absolute; left: 0; right: 0; bottom: 0; height: 122px;
    display: flex;
  }
  .contact-cell {
    flex: 1; display: flex; align-items: center; justify-content: center;
    font-size: 19px; color: var(--white);
  }
  .contact-cell--green { background: var(--green); }
  .contact-cell--black { background: var(--black); }
</style>
</head>
<body>

  <section class="card card--back" aria-label="Card back">
    <div class="top-rule"></div>
    <div class="back-mark">
      <span class="back-mark__square"></span>
      <span class="back-mark__name">BLQ</span>
    </div>
    <p class="back-url">www.<span class="accent">amberharborsupply-example</span>.com</p>
    <div class="bottom-rule"><span></span><span></span><span></span></div>
  </section>

  <section class="card card--front" aria-label="Card front">
    <div class="top-rule"></div>
    <div class="front-brand">
      <span class="front-brand__square"></span>
      <span class="front-brand__name">Amber Harbor Supply</span>
    </div>
    <div class="name-band">
      <span class="name-band__person">Wade Pelham</span>
      <span class="name-band__company">Amber Harbor Supply</span>
    </div>
    <p class="email-row"><span class="label">Email:</span>&nbsp;info@amberharborsupply-example.com</p>
    <div class="contact-row">
      <p class="contact-cell contact-cell--green"><span class="label">Mobile:</span>&nbsp;917-555-4820</p>
      <p class="contact-cell contact-cell--black"><span class="label">Office:</span>&nbsp;516-555-7164</p>
      <p class="contact-cell contact-cell--green"><span class="label">Fax:</span>&nbsp;866-555-3291</p>
    </div>
  </section>

</body>
</html>
```